Brochure design for joint venture

We need a 4 page A4 brochure for a joing venture between two engineering companies.A draft version of the text can be found in the attachments, along with the logo. The text pdf shows the general style and layout of hte text, but am very open to artistic advice.Image placeholders should be added on pages indicated - these are not yet availableColour scheme is orange and green, looking for strong, bold, lines. Look and feel should be clean and professional, not too cluttered.Final desing shoul dbe avialable in RGB psd format, with full layers so we can modify text and images easily.
Like the look of this style:
https://www.plarnivo.com/vector-art/483921-orange-and-green-business-brochure-design-template

```html
<!DOCTYPE html>
<html lang="en">
<head>
<meta charset="utf-8">
<title>A Partnership of Electrical Machine Design Specialists</title>
<link href="https://fonts.googleapis.com/css2?family=Montserrat:wght@600;700&family=Roboto:wght@500;700&display=swap" rel="stylesheet">
<style>
:root{
  --backdrop:#e6e3de;
  --paper:#ffffff;
  --green:#0f8b6c;
  --ink:#2a2a2a;
  --partner-a:#2b2b2b;
  --partner-b:#1f5fa8;
  --orange:#f3a878;
  --yellow:#f8e6a6;
  --sky:#9fb4c8;
  --teal:#7fcbbb;
}
*{margin:0;padding:0;box-sizing:border-box}
html,body{width:1200px;height:880px;overflow:hidden;background:var(--backdrop)}
.canvas{position:relative;width:1200px;height:880px}
.cover{
  position:absolute;left:220px;top:50px;width:780px;height:780px;
  background:var(--paper);padding:14px;
  box-shadow:0 10px 30px rgba(0,0,0,.18);
}
.cover-art{
  position:relative;width:100%;height:100%;overflow:hidden;
  background:
    radial-gradient(circle at 58% 30%, rgba(255,250,215,.95) 0%, rgba(255,240,180,.6) 22%, transparent 45%),
    radial-gradient(circle at 15% 85%, var(--teal) 0%, transparent 40%),
    linear-gradient(160deg, var(--orange) 0%, #f7c98e 28%, var(--yellow) 45%, #c9cfc9 68%, var(--sky) 100%);
}
.hero-photo{position:absolute;inset:0}
.partner{
  position:absolute;display:flex;align-items:center;gap:10px;
  font-family:'Montserrat',sans-serif;font-weight:700;
}
.partner-mark{width:14px;height:14px;border-radius:50%}
.partner--voltaris{left:60px;top:120px;font-size:30px;color:var(--partner-a)}
.partner--voltaris .partner-mark{background:var(--partner-a)}
.partner--corvane{left:400px;top:52px;font-size:26px;color:var(--partner-b);line-height:1.1}
.partner--corvane .partner-mark{background:var(--partner-b)}
.headline{
  position:absolute;left:0;right:0;top:250px;text-align:center;
  font-family:'Montserrat',sans-serif;font-weight:700;color:var(--green);
  font-size:38px;line-height:1.2;
}
.subhead{
  position:absolute;left:0;right:0;top:360px;text-align:center;
  font-family:'Roboto',sans-serif;font-weight:700;color:var(--ink);
  font-size:18px;line-height:1.35;
}
.intro{
  position:absolute;left:300px;right:40px;bottom:70px;
  font-family:'Roboto',sans-serif;font-weight:500;color:#fff;
  font-size:16px;line-height:1.4;
}
</style>
</head>
<body>
<div class="canvas">
  <article class="cover">
    <div class="cover-art">
      <div class="hero-photo" role="img" aria-label="Photo of a hand reaching toward glowing engineering gears in warm orange and cool blue light"></div>

      <div class="partner partner--voltaris"><span class="partner-mark"></span>Voltaris</div>
      <div class="partner partner--corvane"><span class="partner-mark"></span>Corvane Cooling Systems</div>

      <h1 class="headline">A Partnership of<br>Electrical Machine Design Specialists</h1>
      <p class="subhead">Two complementary specialist companies working together to<br>provide state-of-the art complete designs for electrical machines</p>

      <p class="intro">Located in Germany and UK,<br>we are two complimentary electrical machines design companies,<br>combining to provide electrical machine design services.</p>
    </div>
  </article>
</div>
</body>
</html>
```